RQT Livestock needs Buisness Card design using new logo

We need a business card design that ties our website and our new logo together. www.rqtlivestock-example.com The logo will be added to our website at a later date and replace the existing rqt livestock that is on the webpage. We are looking for a simple & professional design.

Target Market(s)

Cattle Producers, Ranchers

Industry/Entity Type

Agriculture

Contact Information for Business Card

Side one:
logo
www.rqtlivestock-example.com

Side two:
RQT Livestock
Robert & Tanya Quill
Hartney, MB Canada
(555) 318-2094/(555) 627-4185
quill47@fernwire-example.net

Font styles to use
Serif
Sans Serif
Script

Requirements
Must have
• We would like to tie our new logo in with our website on the business card.

```html
<!DOCTYPE html>
<html lang="en">
<head>
<meta charset="utf-8">
<title>RQT Livestock – Business Card</title>
<link rel="stylesheet" href="https://fonts.googleapis.com/css2?family=Lato:wght@400;700&display=swap">
<style>
  :root {
    --backdrop: #1c1c1c;
    --card: #f4f4f4;
    --ink: #3a3a3a;
    --ink-dark: #2a2a2a;
    --accent: #d3202a;
    --band-dark: #2b2b2b;
  }
  * { box-sizing: border-box; margin: 0; padding: 0; }
  html, body {
    width: 1200px; height: 873px; overflow: hidden;
    background: var(--backdrop);
    font-family: "Lato", sans-serif;
  }
  .sheet {
    position: relative; width: 1200px; height: 873px;
    display: flex; align-items: center; justify-content: center; gap: 50px;
  }
  .card {
    position: relative; width: 525px; height: 300px;
    background: linear-gradient(160deg, #fbfbfb, var(--card));
    overflow: hidden;
  }
  .card-bands { position: absolute; left: 0; bottom: 0; width: 525px; height: 40px; }
  .brand {
    position: absolute; left: 0; right: 0; text-align: center;
    color: var(--ink); font-weight: 400; letter-spacing: 1px;
    display: flex; align-items: center; justify-content: center; gap: 12px;
  }
  .brand-dot { width: 12px; height: 12px; border-radius: 50%; background: var(--accent); }
  .card-front .brand { top: 100px; font-size: 42px; }
  .website {
    position: absolute; left: 0; right: 0; top: 222px; text-align: center;
    color: var(--accent); font-weight: 700; font-size: 15px; letter-spacing: 3px;
  }
  .card-back .brand { top: 58px; font-size: 36px; }
  .holder {
    position: absolute; right: 32px; top: 168px; text-align: right;
  }
  .holder-name { color: var(--accent); font-weight: 700; font-size: 17px; }
  .holder-role { color: var(--ink-dark); font-size: 12px; margin-top: 3px; }
  .contacts {
    position: absolute; left: 36px; top: 184px; list-style: none;
    color: var(--ink); font-weight: 700; font-size: 14px;
  }
  .contacts li { display: flex; align-items: center; gap: 12px; height: 26px; }
  .contacts svg { width: 15px; height: 15px; fill: var(--accent); }
</style>
</head>
<body>
<main class="sheet">
  <section class="card card-front" aria-label="Business card front">
    <div class="brand"><span class="brand-dot"></span>RQT Livestock</div>
    <p class="website">www.rqtlivestock-example.com</p>
    <svg class="card-bands" viewBox="0 0 525 40" aria-hidden="true">
      <rect x="0" y="30" width="525" height="10" fill="var(--band-dark)"/>
      <path d="M345 40 Q350 22 372 22 H525 V40 Z" fill="var(--accent)"/>
    </svg>
  </section>

  <section class="card card-back" aria-label="Business card back">
    <div class="brand"><span class="brand-dot"></span>RQT Livestock</div>
    <div class="holder">
      <p class="holder-name">Robert &amp; Tanya Quill</p>
      <p class="holder-role">Account Manager Qld / Northern NSW</p>
    </div>
    <ul class="contacts">
      <li>
        <svg viewBox="0 0 16 16" aria-hidden="true"><path d="M2 5c0-2 2-3 6-3s6 1 6 3v1h-3V5H5v1H2zM4 7h8l2 6H2z"/></svg>
        (555) 318-2094
      </li>
      <li>
        <svg viewBox="0 0 16 16" aria-hidden="true"><path d="M4 1h8v14H4zM5.5 3v9h5V3zM7 13h2v1H7z" fill-rule="evenodd"/></svg>
        (555) 627-4185
      </li>
      <li>
        <svg viewBox="0 0 16 16" aria-hidden="true"><path d="M1 3h14v10H1zM2 4l6 5 6-5z" fill-rule="evenodd"/></svg>
        quill47@fernwire-example.net
      </li>
    </ul>
    <svg class="card-bands" viewBox="0 0 525 40" aria-hidden="true">
      <rect x="0" y="30" width="525" height="10" fill="var(--band-dark)"/>
      <path d="M345 40 Q350 22 372 22 H525 V40 Z" fill="var(--accent)"/>
    </svg>
  </section>
</main>
</body>
</html>
```